Daily Care Record Sheets

As a preschool, we have notes that we send home on a daily basis so the parents know what is going on. We would like to reformat the preschool and toddler sheets<br/><br/>The preschool participation sheet is 4.25"x 5.6"<br/>We have attached an example of what we are using currently and the information we would like on our new sheet. We would like the logo added as well.<br/><br/>The Bramble Notes sheet should be a half page. I have included 2 examples as well as a sheet of what we would like on it moving forward. <br/><br/>Please do not hesitate to reach out if you have any questions on any of this. They will print in black and white on colored paper.<br/><br/>Thanks!<br/>Marla

Target Market(s)

Parents of the toddlers and preschools in our care

Industry/Entity Type

Preschool

Colors

Designer to choose only greyscale colors for use in the design.

Requirements
Must have
• Logo
• The items in the "FOR NEW VERSION" files

```html
<!DOCTYPE html>
<html lang="en">
<head>
<meta charset="utf-8">
<title>Toddler Daily Care Record</title>
<link href="https://fonts.googleapis.com/css2?family=Poppins:wght@600;700&family=Arimo:wght@400;700&display=swap" rel="stylesheet">
<style>
  :root {
    --ink: #1a1a1a;
    --ink-soft: #444444;
    --rule: #555555;
    --paper: #ffffff;
    --wave-light: #efefef;
    --wave-mid: #e0e0e0;
    --art-top: #d6d6d6;
    --art-bottom: #9a9a9a;
  }
  * { box-sizing: border-box; margin: 0; padding: 0; }
  html, body { width: 1012px; height: 1200px; overflow: hidden; background: var(--paper); }
  body { position: relative; font-family: "Arimo", Arial, sans-serif; color: var(--ink); }

  .brand { position: absolute; top: 82px; left: 0; width: 1012px; text-align: center; }
  .brand-mark { display: inline-flex; align-items: center; gap: 10px; font-family: "Arimo", Arial, sans-serif; font-weight: 700; font-size: 26px; color: var(--ink); }
  .brand-dot { width: 18px; height: 18px; border-radius: 50%; background: var(--ink); }
  .brand-tagline { margin-top: 6px; font-size: 10px; letter-spacing: 2px; text-transform: uppercase; color: var(--ink-soft); }
  .brand-tagline::before { content: ""; display: block; width: 300px; height: 2px; background: var(--ink); margin: 0 auto 5px; }

  .sheet-title { position: absolute; top: 186px; left: 0; width: 1012px; text-align: center; font-family: "Poppins", sans-serif; font-weight: 700; font-size: 46px; letter-spacing: 0.5px; }

  .field-row { position: absolute; top: 290px; left: 105px; font-weight: 700; font-size: 24px; display: flex; gap: 14px; }
  .blank { display: inline-block; border-bottom: 2px solid var(--ink); height: 22px; }

  .col-heading { font-weight: 700; font-size: 21px; margin-bottom: 10px; }
  .caregiver { position: absolute; top: 358px; left: 105px; }
  .caregiver .col-heading { font-size: 17px; }
  .snack-row { display: flex; align-items: center; height: 30px; font-size: 15px; }
  .snack-row .label { width: 112px; font-weight: 700; font-size: 16px; }
  .option { display: inline-flex; align-items: center; gap: 4px; margin-right: 12px; }
  .radio { width: 13px; height: 13px; border: 1.5px solid var(--ink-soft); border-radius: 50%; }

  .disposition { position: absolute; top: 358px; left: 528px; }
  .word-list { font-size: 17px; line-height: 24px; color: var(--ink); }

  .nap { position: absolute; top: 520px; left: 105px; display: flex; gap: 16px; }
  .nap .col-heading { font-size: 21px; }
  .nap-options { font-size: 14px; line-height: 30px; padding-top: 1px; }
  .nap-options .option { margin-right: 16px; }

  .outside { position: absolute; top: 520px; left: 528px; }

  .diaper { position: absolute; top: 640px; left: 105px; }
  .diaper .col-heading { font-size: 19px; }
  .diaper-table { border-collapse: collapse; width: 806px; }
  .diaper-table th, .diaper-table td { border: 1.5px solid var(--rule); width: 62px; text-align: center; }
  .diaper-table th { font-size: 12px; font-weight: 700; height: 24px; }
  .diaper-table td { height: 66px; }

  .waves { position: absolute; top: 790px; left: 0; }
  .boat-art { position: absolute; top: 760px; left: 800px; width: 150px; height: 170px; border-radius: 16px 16px 70px 70px; background: linear-gradient(180deg, var(--art-top), var(--art-bottom)); }

  .notes { position: absolute; top: 970px; left: 105px; width: 806px; }
  .note-line { display: flex; align-items: flex-end; height: 50px; font-weight: 700; font-size: 21px; }
  .note-line .dots { flex: 1; border-bottom: 2px dotted var(--ink-soft); margin-left: 6px; margin-bottom: 5px; }
</style>
</head>
<body>
  <header class="brand">
    <div class="brand-mark"><span class="brand-dot"></span>Sunny Lane Learning</div>
    <div class="brand-tagline">Growing bright minds every day</div>
  </header>

  <h1 class="sheet-title">Toddler Daily Care Record</h1>

  <div class="field-row">
    <span>Child<span class="blank" style="width:300px"></span></span>
    <span>Date<span class="blank" style="width:120px"></span></span>
  </div>

  <section class="caregiver">
    <div class="col-heading">Caregiver Use</div>
    <div class="snack-row"><span class="label">AM Snack:</span><span class="option"><span class="radio"></span>All</span><span class="option"><span class="radio"></span>Most</span><span class="option"><span class="radio"></span>Some</span><span class="option"><span class="radio"></span>None</span></div>
    <div class="snack-row"><span class="label">Lunch:</span><span class="option"><span class="radio"></span>All</span><span class="option"><span class="radio"></span>Most</span><span class="option"><span class="radio"></span>Some</span><span class="option"><span class="radio"></span>None</span></div>
    <div class="snack-row"><span class="label">PM Snack:</span><span class="option"><span class="radio"></span>All</span><span class="option"><span class="radio"></span>Most</span><span class="option"><span class="radio"></span>Some</span><span class="option"><span class="radio"></span>None</span></div>
  </section>

  <section class="disposition">
    <div class="col-heading">Disposition:</div>
    <div class="word-list">
      Happy / Curious / Friendly/ Sleepy<br>
      Busy / Cheerful / Energetic / Quiet<br>
      Inquisitive / Talkative / Mischievous<br>
      Difficulty Followed Directions
    </div>
  </section>

  <section class="nap">
    <div class="col-heading">Nap Time:</div>
    <div class="nap-options">
      <div><span class="option"><span class="radio"></span>2 hrs</span><span class="option"><span class="radio"></span>1 ½ hrs</span><span class="option"><span class="radio"></span>1 hr</span></div>
      <div><span class="option"><span class="radio"></span>I was Quiet</span></div>
      <div><span class="option"><span class="radio"></span>I didn't feel like resting</span></div>
    </div>
  </section>

  <section class="outside">
    <div class="col-heading">Outside Play</div>
    <div class="word-list">
      Music / Art / Dancing / Painting Blocks<br>
      Sandbox / Cars / Swings
    </div>
  </section>

  <section class="diaper">
    <div class="col-heading">Diaper Checks:</div>
    <table class="diaper-table">
      <tr><th>6:30</th><th>7:00</th><th>8:00</th><th>9:00</th><th>10:00</th><th>11:00</th><th>12:00</th><th>1:00</th><th>2:00</th><th>3:00</th><th>4:00</th><th>5:00</th><th>6:00</th></tr>
      <tr><td></td><td></td><td></td><td></td><td></td><td></td><td></td><td></td><td></td><td></td><td></td><td></td><td></td></tr>
    </table>
  </section>

  <svg class="waves" width="1012" height="110" viewBox="0 0 1012 110" aria-hidden="true">
    <path d="M0 30 C120 0 240 60 380 30 S640 0 780 30 S940 55 1012 25 V110 H0 Z" fill="var(--wave-light)"/>
    <path d="M0 60 C140 35 260 85 420 58 S680 35 820 62 S960 80 1012 55 V110 H0 Z" fill="var(--wave-mid)"/>
  </svg>

  <div class="boat-art" role="img" aria-label="Illustration of a cartoon animal sailing a small boat with a flag"></div>

  <section class="notes">
    <div class="note-line">Your child needs:<span class="dots"></span></div>
    <div class="note-line">Today I had fun:<span class="dots"></span></div>
    <div class="note-line">Caregivers Observations:<span class="dots"></span></div>
  </section>
</body>
</html>
```